Equestrian industry - Problem solving and creative skills required!

I have just joined a saddle fitting franchise that has an existing logo that I would like to tweak (see Summit Tackworks file for the original logo). The franchise doesn't have any real colour scheme except that the horse logo (attached - logoonly) must stay orange and the words 'Summit Tackworks' must stay white. Apart from that I have free reign to use what ever colours etc I like. I have chosen some colours that I would like to work with (see chosen colours file). I don't want anything drastically different because I still have to represent myself as part of the franchise, however I would like to make it more modern and make it my own.

My business name is 'Summit Tackworks Western Australia' but the Western Australia can be shortened to 'WA'. My business is about integrity, expert knowledge and empathy.

Could you please play with the chosen colours and the existing logo to create a logo that is less 80's and more in this decade. I would also like you to create a stationary package including a form header, letterhead and business card etc.

I am also able to provide the logo in vector format if required.

Thank you!

Target Market(s)

Grass Roots horse riders - usually middle aged women

Industry/Entity Type

Industry

Contact Information for Business Card

Dana Whitcombe
Phone: 0417385926
email:dana@summittackworks.net.au
Facebook page and web address to come

Logo Text

Summit Tackworks Western Australia

Logo styles of interest
Emblem Logo
Pictorial/Combination Logo
Abstract Logo
Requirements
Must have
• Existing jumping horse image incorporated.
• Colour of horse logo to stay the same.
• Prefer to keep the words 'Summit Tackworks' white.
Nice to have
• more modern
• using chosen colours
Should not have
• changed the existing jumping horse image
• be too far removed from the original logo

```html
<!DOCTYPE html>
<html lang="en">
<head>
<meta charset="utf-8">
<title>Summit Tackworks – Business Card</title>
<link rel="stylesheet" href="https://fonts.googleapis.com/css2?family=Courier+Prime:wght@400;700&family=Fondamento&display=swap">
<style>
  :root {
    --backdrop: #3d3431;
    --card-white: #ffffff;
    --card-pink: #f4c8c6;
    --edge-white: #f7f3f3;
    --rose-panel: #b86467;
    --panel-frame: #8d8a8a;
    --brand-orange: #f08a1e;
    --ink-dark: #2b2b2b;
    --mark-grey: #8a8887;
  }
  * { box-sizing: border-box; margin: 0; padding: 0; }
  html, body { width: 1200px; height: 1000px; overflow: hidden; }
  body { background: var(--backdrop); position: relative; }

  .card {
    position: absolute;
    width: 540px;
    height: 310px;
    box-shadow: 0 14px 30px rgba(0,0,0,0.45);
    overflow: hidden;
  }

  .brand-name {
    font-family: "Fondamento", serif; font-weight: 400;
    color: var(--brand-orange); text-align: center;
    white-space: nowrap;
  }
  .mark-space {
    display: block;
    background: var(--mark-grey);
    opacity: 0.85;
  }

  /* Contact side */
  .card-contact { left: 50px; top: 130px; background: var(--card-white); }
  .logo-panel {
    position: absolute; right: 0; top: 0;
    width: 290px; height: 165px;
    background: var(--rose-panel);
    border-left: 10px solid var(--panel-frame);
    border-bottom: 10px solid var(--panel-frame);
    display: flex; flex-direction: column; align-items: center; justify-content: center; gap: 8px;
  }
  .logo-panel .mark-space { width: 76px; height: 76px; }
  .logo-panel .brand-name { font-size: 17px; line-height: 1.15; }

  .holder-name {
    position: absolute; left: 36px; top: 120px;
    font-family: "Courier Prime", monospace; font-weight: 700;
    font-size: 20px; color: var(--brand-orange); letter-spacing: 1px;
  }
  .contact-list {
    position: absolute; left: 36px; top: 190px;
    list-style: none;
    font-family: "Courier Prime", monospace; font-size: 14px; color: var(--ink-dark);
  }
  .contact-list li { display: flex; align-items: center; gap: 8px; margin-bottom: 14px; }
  .contact-list svg { width: 16px; height: 16px; flex: none; }

  /* Brand side */
  .card-brand {
    left: 610px; top: 430px;
    background: linear-gradient(90deg, var(--edge-white) 0%, var(--card-pink) 10%, var(--card-pink) 88%, var(--edge-white) 100%);
  }
  .edge-texture { position: absolute; top: 0; bottom: 0; width: 60px; }
  .edge-texture.left { left: 0; background: linear-gradient(90deg, rgba(255,255,255,0.6), rgba(255,255,255,0)); }
  .edge-texture.right { right: 0; background: linear-gradient(270deg, rgba(255,255,255,0.6), rgba(255,255,255,0)); }

  .brand-lockup {
    position: absolute; left: 0; right: 0; top: 30px;
    display: flex; flex-direction: column; align-items: center; gap: 14px;
  }
  .card-brand .mark-space { width: 150px; height: 150px; }
  .card-brand .brand-name { font-size: 32px; line-height: 1.12; }
</style>
</head>
<body>

  <section class="card card-contact" aria-label="Business card, contact side">
    <div class="logo-panel">
      <span class="mark-space" role="img" aria-label="Space for the brand's horse-and-rider mark"></span>
      <span class="brand-name">Summit Tackworks<br>Western Australia</span>
    </div>

    <p class="holder-name">Dana Whitcombe</p>

    <ul class="contact-list">
      <li>
        <svg viewBox="0 0 16 16" aria-hidden="true"><path d="M8 1a5 5 0 0 0-5 5c0 4 5 9 5 9s5-5 5-9a5 5 0 0 0-5-5zm0 7a2 2 0 1 1 0-4 2 2 0 0 1 0 4z" fill="#2b2b2b"/></svg>
        9 Brook Lane Glenforth WA 6081
      </li>
      <li>
        <svg viewBox="0 0 16 16" aria-hidden="true"><path d="M4 1l2.5 3-1.5 2c1 2 2.5 3.5 4.5 4.5l2-1.5 3 2.5-1.5 2.5C7 14 2 9 1.5 2.5z" fill="#2b2b2b"/></svg>
        0417385926
      </li>
      <li>
        <svg viewBox="0 0 16 16" aria-hidden="true"><rect x="1" y="3" width="14" height="10" rx="1.5" fill="#2b2b2b"/><path d="M2 4l6 5 6-5" fill="none" stroke="#fff" stroke-width="1.3"/></svg>
        dana@summittackworks.net.au
      </li>
    </ul>
  </section>

  <section class="card card-brand" aria-label="Business card, brand side">
    <div class="edge-texture left" role="img" aria-label="Soft dotted texture along the left edge"></div>
    <div class="edge-texture right" role="img" aria-label="Soft dotted texture along the right edge"></div>
    <div class="brand-lockup">
      <span class="mark-space" role="img" aria-label="Space for the brand's horse-and-rider mark"></span>
      <span class="brand-name">Summit Tackworks<br>Western Australia</span>
    </div>
  </section>

</body>
</html>
```